Engineering Land Development Company Needs Flyer Brochure for Prospective Professional Clients

Our company provides land development site design for commercial projects. We have many repeat clients that are familiar with our work. We do not advertise our services other than a website. Most of our referrals are from existing clients. When a new client contacts us and asks for a proposal for a project we would like to have a brochure that shows our strengths, experience, and professionalism. We are selling professional services similar to a lawyer or accountant. We want new clients to feel comfortable hiring a new firm. The brochure would be one page single-side included when we submit proposals for new projects. Check out our website at tovamrk.net for more info. We would like a brochure that mixes grading/excavation construction work on a job site with business professional. We will need to update the brochure so we want it in .doc .psd or some other edit format. The brochure we are using is attached. It is very two-dimensional. We need some depth.

Target Market(s)

Land developers, architects, real estate, professionals, attorneys

Industry/Entity Type

Real Estate Development

Font styles to use
Sans Serif
Other font styles liked:
• calibri

Colors
0355a3
9bcb3c

Requirements
Must have
• company logo, ability to update text and images
Nice to have
• background image(s) with text overlay
Should not have
• cartoons, harsh colors, stock photos of people, lots of boxes

```html
<!DOCTYPE html>
<html lang="en">
<head>
<meta charset="utf-8">
<title>Tovamark Engineering PLLC – Land Development Services</title>
<link rel="stylesheet" href="https://fonts.googleapis.com/css2?family=Lato:wght@400;700;900&family=Roboto+Condensed:wght@700&family=Open+Sans:wght@300;400&display=swap">
<style>
  :root {
    --brand-blue: #0355a3;
    --deep-blue: #2f3f9a;
    --indigo: #3a4aa6;
    --leaf-green: #3db34a;
    --lime: #9bcb3c;
    --ink: #1d1d1f;
    --muted: #555a66;
    --paper: #ffffff;
  }
  * { margin: 0; padding: 0; box-sizing: border-box; }
  html, body { width: 900px; height: 1200px; overflow: hidden; background: var(--paper); }
  body { font-family: "Lato", Arial, sans-serif; color: var(--ink); }

  .flyer { position: relative; width: 900px; height: 1200px; overflow: hidden; background: var(--paper); }

  .hero-photo {
    position: absolute; left: 0; top: 0; width: 900px; height: 540px;
    background: linear-gradient(180deg, #3f86d8 0%, #6aa7e6 38%, #8fb57a 55%, #c98a52 70%, #b06a3a 100%);
  }
  .hero-wave { position: absolute; left: 0; top: 440px; width: 900px; height: 110px; }

  .brand {
    position: absolute; top: 510px; left: 0; width: 900px;
    display: flex; justify-content: center; align-items: center; gap: 10px;
  }
  .brand-square { width: 32px; height: 32px; background: var(--indigo); }
  .brand-name {
    font-family: "Open Sans", Arial, sans-serif; font-weight: 300;
    font-size: 27px; color: var(--indigo); letter-spacing: -0.3px;
  }

  .mission-box {
    position: absolute; left: 47px; top: 560px; width: 355px; height: 66px;
    background: var(--indigo); border-radius: 12px;
    display: flex; align-items: center; justify-content: center; text-align: center;
    font-family: "Roboto Condensed", Arial, sans-serif; font-weight: 700;
    color: #fff; font-size: 15.5px; line-height: 19px; text-transform: uppercase;
  }
  .intro {
    position: absolute; left: 47px; top: 636px; width: 355px;
    font-size: 13px; line-height: 16px; text-align: justify;
  }
  .rule { position: absolute; left: 47px; top: 746px; width: 355px; height: 1.5px; background: var(--indigo); }
  .clients-lead {
    position: absolute; left: 47px; top: 754px; width: 355px;
    font-size: 12px; line-height: 15px; font-weight: 700;
  }
  .client-row {
    position: absolute; display: flex; gap: 2px;
  }
  .client {
    width: 43px; height: 32px; display: flex; align-items: center; justify-content: center;
    text-align: center; font-weight: 900; font-size: 8px; line-height: 9px; color: var(--brand-blue);
  }
  .client.red { color: #c0392b; }
  .client.green { color: #2e7d32; }

  .project-photo { position: absolute; left: 0; top: 850px; width: 470px; height: 350px; }

  .services { position: absolute; left: 448px; top: 566px; width: 437px; }
  .service { margin-bottom: 14px; }
  .service h2 {
    position: relative; padding-left: 20px;
    font-size: 14.5px; line-height: 16px; font-weight: 900; color: var(--indigo);
  }
  .service h2::before {
    content: ""; position: absolute; left: 0; top: 2px; width: 13px; height: 13px;
    border-radius: 50%; background: var(--leaf-green);
  }
  .service p { margin-top: 6px; font-size: 13px; line-height: 16px; text-align: justify; }

  .footer-line { position: absolute; left: 430px; top: 1140px; width: 470px; height: 8px; background: var(--indigo); }
  .footer {
    position: absolute; left: 430px; top: 1148px; width: 470px; height: 52px;
    background: var(--leaf-green); color: #fff;
    display: flex; align-items: center; padding-left: 30px;
    font-size: 12.5px; line-height: 15px; font-weight: 700;
  }
  .footer-item { display: flex; align-items: flex-start; gap: 7px; }
  .footer-item svg { flex: none; margin-top: 1px; }
  .footer-divider { width: 1.5px; height: 36px; background: #fff; margin: 0 18px; }
  .contact-lines div { display: flex; align-items: center; gap: 7px; }
</style>
</head>
<body>
<div class="flyer">

  <div class="hero-photo" role="img" aria-label="Photo of a yellow excavator lifting a dirt-filled bucket on a red clay grading site under a blue sky"></div>
  <svg class="hero-wave" viewBox="0 0 900 110" preserveAspectRatio="none" aria-hidden="true">
    <path d="M0,62 C250,20 600,20 900,52 L900,110 L0,110 Z" fill="var(--leaf-green)"/>
    <path d="M0,70 C250,32 600,32 900,66 L900,110 L0,110 Z" fill="var(--paper)"/>
  </svg>

  <div class="brand">
    <span class="brand-square"></span>
    <span class="brand-name">Tovamark Engineering PLLC</span>
  </div>

  <div class="mission-box">Our mission at Tovamark Engineering<br>is to provide superior quality<br>professional land development services</div>

  <p class="intro">Our firm provides planning, surveying, engineering, and environmental services which allows us to focus on the entire land development process rather than one specific discipline. Providing a broad scope of professional services helps to streamline a project by eliminating many disadvantages of having multiple firms with overlapping responsibilities.</p>

  <div class="rule"></div>
  <p class="clients-lead">Our business would not be successful without the support of our clients. Some of our project clients include</p>

  <div class="client-row" style="left:47px; top:788px;">
    <span class="client green">Parkway Trust</span>
    <span class="client">Kettle Deli</span>
    <span class="client red">Bun Stop</span>
    <span class="client">Griddle House</span>
    <span class="client red">Salsa Jo's</span>
    <span class="client red">Crust Co</span>
    <span class="client red">Motorline Parts</span>
    <span class="client green">Fieldline Tractor</span>
  </div>
  <div class="client-row" style="left:47px; top:828px;">
    <span class="client">Homestead Supply</span>
    <span class="client red">Kanto Motors</span>
    <span class="client">Linewave</span>
    <span class="client red">Harlow Farms</span>
    <span class="client red">Ember Grill</span>
    <span class="client">Verde Taco</span>
    <span class="client">Pantry Fresh</span>
  </div>
  <div class="client-row" style="left:225px; top:870px;">
    <span class="client green">Roastery</span>
    <span class="client">Wingyard</span>
    <span class="client red">Waffle Porch</span>
    <span class="client red">PetNest</span>
  </div>

  <svg class="project-photo" viewBox="0 0 470 350" aria-hidden="true">
    <defs>
      <linearGradient id="steelBuild" x1="0" y1="0" x2="0" y2="1">
        <stop offset="0" stop-color="#9ec3e6"/>
        <stop offset="0.55" stop-color="#b9c4cf"/>
        <stop offset="1" stop-color="#8c7f70"/>
      </linearGradient>
    </defs>
    <path d="M0,10 C220,0 400,100 455,298 L455,350 L0,350 Z" fill="var(--leaf-green)"/>
    <path d="M0,22 C215,12 390,108 443,298 L443,350 L0,350 Z" fill="var(--indigo)"/>
    <path d="M0,34 C210,26 378,116 430,298 L430,350 L0,350 Z" fill="url(#steelBuild)" role="img" aria-label="Photo of a steel-framed greenhouse structure under construction with lifts and workers"/>
  </svg>

  <div class="services">
    <section class="service">
      <h2>We are land development professionals who can see the “big picture”.</h2>
      <p>We have extensive experience with site selection, due diligence investigations, re-zonings, and land planning. Every project is different. We look forward to identifying all feasible alternatives. We become part of the project and enjoy developing the best plan for the success of each particular project. We understand that time is money and unexpected delays are unacceptable.</p>
    </section>
    <section class="service">
      <h2>We are land development professionals who provide superior quality surveying services.</h2>
      <p>Our firm can handle any surveying need. We have extensive experience with ALTA surveys, boundary surveys, subdivision platting, topographic/location surveys, GPS surveys, R/W surveys, construction staking, as-built surveys, elevation certificates, etc. We work closely with title attorneys to provide legal descriptions, exhibits, and other assistance when closing the real estate deal.</p>
    </section>
    <section class="service">
      <h2>We are land development professionals who can handle the most complicated engineering challenge.</h2>
      <p>Let us worry about all the technical stuff and the regulators. Our firm has extensive experience with infrastructure assessments, erosion control, grading, roadway design, stormwater management, water systems, sewer systems, utilities, flood plain management, landscape design, permitting, bidding, and construction administration.</p>
    </section>
    <section class="service">
      <h2>We are land development professionals who provide superior quality environmental services.</h2>
      <p>We provide environmental site assessments, underground storage tank management, soil and groundwater sampling and testing, contamination remediation, Brownfields assessments, permitting and redevelopment, and wetlands permitting. Our firm works closely with state and federal agencies to provide economical mitigation and remediation solutions.</p>
    </section>
  </div>

  <div class="footer-line"></div>
  <footer class="footer">
    <div class="footer-item">
      <svg width="10" height="14" viewBox="0 0 10 14" aria-hidden="true"><path d="M5,0 C2.2,0 0,2.2 0,5 C0,8.5 5,14 5,14 C5,14 10,8.5 10,5 C10,2.2 7.8,0 5,0 Z M5,7 A2,2 0 1 1 5,3 A2,2 0 1 1 5,7 Z" fill="#fff"/></svg>
      <div>418 Ridgeview Avenue – Suite 120<br>Cedar Hollow, NC 28000</div>
    </div>
    <div class="footer-divider"></div>
    <div class="contact-lines">
      <div>
        <svg width="12" height="11" viewBox="0 0 12 11" aria-hidden="true"><path d="M1,3 C1,1 3,0.5 6,0.5 C9,0.5 11,1 11,3 L9,4 L8,2.5 L4,2.5 L3,4 Z M2,5 L10,5 L11,10.5 L1,10.5 Z" fill="#fff"/></svg>
        <span>(555) 014-2760</span>
      </div>
      <div>
        <svg width="12" height="12" viewBox="0 0 12 12" aria-hidden="true"><circle cx="6" cy="6" r="5.5" fill="#fff"/><path d="M0.5,6 H11.5 M6,0.5 C3,3 3,9 6,11.5 M6,0.5 C9,3 9,9 6,11.5" stroke="var(--leaf-green)" stroke-width="1" fill="none"/></svg>
        <span>www.tovamrk.net</span>
      </div>
    </div>
  </footer>

</div>
</body>
</html>
```